meridale partners business card

Architectural firm business card
Updates

Please note:

corporate colour black+yellow are the only elements to be kept.
NO OTHER ELEMENT TO BE REUSED FROM PREVIOUS BUSINESS CARD.
Thank you.

Dear Everyone,

Thank you for your participation. I have upload the KBSO+ logo again for incoporate in the card. in tif and pdf format.

Thank you 

I keep getting request for the logo file. Does everyone has the same problem?

I cannot do much, because the file is upload to the website server. I can't seem to see it either.

The logo file is now working. Please download. I check it myself. Thank you everyone.

Dear All,

Thank you for all the hard work. There are a lot of great work. Due to current commitment with work, I am unable to review them just yet. I will do so next week and advise everyone also. Thank you again. Best regards

Dear All,

Thank you for your participation. There are a lot of good design. Unfortunately, I can only select one. All the best. This is definitely a good crowd to work with. Thank you everyone again.

Best regards

Target Market(s)

Corporate, commercial and institutional projects only

Industry/Entity Type

Business

Requirements
Must have
• elegant simple
double sided with coating
Member of Southland Guild of Draughtsmen (logo only)
corporate colour black and

LOGO FILE UPLOADED
Should not have
• should not be the same as current business card.
upload for reference information only.
font sans serif preferred.

```html
<!DOCTYPE html>
<html lang="en">
<head>
<meta charset="utf-8">
<title>meridale partners business card</title>
<link href="https://fonts.googleapis.com/css2?family=Open+Sans:wght@400;600;700&family=Share+Tech+Mono&display=swap" rel="stylesheet">
<style>
  :root {
    --bg: #d9d9d6;
    --card: #f4f4f2;
    --grid: #d4d4d2;
    --orange: #e8801c;
    --black: #111111;
    --ink: #1a1a1a;
    --white: #ffffff;
  }
  * { margin: 0; padding: 0; box-sizing: border-box; }
  html, body { width: 1200px; height: 1000px; overflow: hidden; }
  body {
    background: var(--bg);
    font-family: "Open Sans", Arial, sans-serif;
    color: var(--ink);
    position: relative;
  }
  .card {
    position: absolute;
    left: 250px;
    width: 700px;
    height: 428px;
    background: var(--card);
    box-shadow: 0 2px 6px rgba(0,0,0,0.15);
  }
  .card--front {
    top: 50px;
    background-color: var(--card);
    background-image:
      linear-gradient(var(--grid) 1px, transparent 1px),
      linear-gradient(90deg, var(--grid) 1px, transparent 1px);
    background-size: 22px 22px;
  }
  .card--back { top: 522px; }

  .brand-mark {
    position: absolute;
    left: 40px; top: 24px;
    width: 40px; height: 40px;
    background: var(--orange);
  }
  .brand-name {
    position: absolute;
    left: 40px; top: 68px;
    font-size: 12px; font-weight: 600;
    color: var(--orange);
  }
  .role {
    position: absolute;
    left: 40px; top: 86px;
    font-size: 17px; font-weight: 700;
  }
  .person-name {
    position: absolute;
    left: 190px; top: 20px;
    font-size: 31px; font-weight: 700;
  }
  .credential, .mobile {
    position: absolute;
    left: 190px;
    font-family: "Share Tech Mono", monospace;
    font-size: 16px;
  }
  .credential { top: 66px; }
  .mobile { top: 86px; font-weight: 700; }

  .office {
    position: absolute;
    left: 40px; top: 150px;
  }
  .office-name { font-size: 19px; font-weight: 700; margin-bottom: 8px; }
  .office-line { font-size: 13px; line-height: 16px; }

  .website {
    position: absolute;
    left: 140px; top: 330px;
    font-size: 28px; font-weight: 700;
  }

  .services {
    position: absolute;
    left: 440px; top: 168px;
    width: 232px; height: 160px;
    background: linear-gradient(90deg, var(--orange) 0 52%, var(--black) 52% 100%);
    color: var(--white);
    text-align: right;
    padding: 22px 10px 0 0;
  }
  .service { font-size: 21px; line-height: 40px; white-space: nowrap; }

  .back-lockup {
    position: absolute;
    left: 0; right: 0; top: 150px;
    text-align: center;
  }
  .back-brand {
    display: inline-flex; align-items: center; gap: 12px;
    font-size: 30px; font-weight: 600; color: var(--orange);
  }
  .back-brand .square {
    width: 30px; height: 30px; background: var(--orange);
  }
  .back-url {
    margin-top: 14px;
    font-size: 28px; font-weight: 600; color: var(--orange);
  }
</style>
</head>
<body>
  <section class="card card--front">
    <div class="brand-mark"></div>
    <div class="brand-name">meridale partners</div>
    <div class="role">Director</div>
    <div class="person-name">Linh Bao</div>
    <div class="credential">Architect (NSW BoA reg. no: 5021)</div>
    <div class="mobile">M: 0412 77 40 26</div>

    <div class="office">
      <div class="office-name">Corwell House</div>
      <div class="office-line">14 Fenwick Lane, Alder Park NSW 2190</div>
      <div class="office-line">Tel:&nbsp; +612 9810 2274</div>
      <div class="office-line">Fax: +612 9810 2275</div>
      <div class="office-line">email: mail@meridalepartners.com.au</div>
    </div>

    <div class="services">
      <div class="service">architects</div>
      <div class="service">urban designers</div>
      <div class="service">project managers</div>
    </div>

    <div class="website">www.meridalepartners.com.au</div>
  </section>

  <section class="card card--back">
    <div class="back-lockup">
      <div class="back-brand"><span class="square"></span>meridale partners</div>
      <div class="back-url">www.meridalepartners.com.au</div>
    </div>
  </section>
</body>
</html>
```